Flyer design for retail store owners

i would need to have a flyer design for my retail shop customers to show that I am a mailbox store that has all major shipping vendors to for their shipping needs. Ensuring that they can take advantage of opening a house account at the store and billed monthly, word document has all the details. Please use stock images for the notary public, passport photos, mailbox brass pictures of my actual mailboxes are listed in the pictures. I need to make it POP and WOW these retail store owners as I am using it to advertise the business

```html
<!DOCTYPE html>
<html lang="en">
<head>
<meta charset="utf-8">
<title>Now Renting Mailboxes – Swift Parcel &amp; Post</title>
<link href="https://fonts.googleapis.com/css2?family=Montserrat:wght@500;700;800&family=Oswald:wght@500;600&family=Poppins:wght@400;600;700&display=swap" rel="stylesheet">
<style>
  :root{
    --teal:#0893a5;
    --teal-light:#6cc7d0;
    --teal-pale:#c9eef2;
    --navy:#0a3b5e;
    --deep-teal:#0a6b88;
    --ink:#222;
    --white:#fff;
    --gold-1:#e7bf78;
    --gold-2:#b57f2c;
  }
  *{margin:0;padding:0;box-sizing:border-box}
  html,body{width:848px;height:1200px;overflow:hidden;background:#fff}
  .flyer{position:relative;width:848px;height:1200px;overflow:hidden;background:var(--white);font-family:"Poppins",sans-serif;color:var(--ink)}

  .header-band{position:absolute;left:0;top:0;width:848px;height:233px;background:linear-gradient(135deg,var(--teal) 0%,#0a86a0 55%,var(--deep-teal) 100%)}
  .header-stripe{position:absolute;background:rgba(10,59,94,.35);border-radius:18px;transform:rotate(45deg)}

  .headline-pill{position:absolute;left:30px;top:27px;width:482px;height:78px;background:var(--navy);border-radius:38px 4px 4px 4px}
  .headline{position:absolute;left:44px;top:28px;font-family:"Montserrat",sans-serif;font-weight:800;font-size:57px;color:#f2f2f2;letter-spacing:-.5px;line-height:78px}
  .subhead{position:absolute;left:44px;top:112px;font-family:"Montserrat",sans-serif;font-weight:500;font-size:59px;color:var(--white);line-height:80px;letter-spacing:.5px}
  .location{position:absolute;right:358px;top:196px;font-family:"Oswald",sans-serif;font-weight:600;font-size:24px;color:var(--white);letter-spacing:-.3px;white-space:nowrap}

  .intro{position:absolute;left:20px;top:258px;width:442px;font-size:13.4px;line-height:24.3px;text-align:justify}
  .intro strong{font-weight:700}

  .photo-main{position:absolute;left:480px;top:60px;width:420px;height:420px;border-radius:50%;border:12px solid var(--teal-light);background:radial-gradient(circle at 40% 45%,var(--gold-1),var(--gold-2) 80%)}
  .photo-open{position:absolute;left:592px;top:450px;width:286px;height:286px;border-radius:50%;border:12px solid var(--teal-light);background:radial-gradient(circle at 50% 50%,#f0cf88,#a8742a 85%)}
  .open-view{position:absolute;left:650px;top:740px;width:190px;height:60px}

  .bubble{position:absolute;border-radius:50%;background:var(--teal-pale)}

  .section-band{position:absolute;left:0;height:48px;background:var(--teal);color:var(--white);font-family:"Oswald",sans-serif;font-weight:500;letter-spacing:2px;font-size:24px;line-height:48px;padding-left:72px;white-space:nowrap}
  .offering-band{top:521px;width:620px;clip-path:polygon(0 0,100% 0,94% 100%,0 100%)}
  .deals-band{top:772px;width:448px;height:52px;line-height:52px;font-size:22px;letter-spacing:1.5px;padding-left:70px}
  .deals-chevron{position:absolute;left:446px;top:772px;width:52px;height:52px}

  .offer-list{position:absolute;left:45px;top:586px;width:540px;list-style:none;font-size:14px;line-height:18px}
  .offer-list li{position:relative;padding-left:27px;margin-bottom:20px}
  .offer-list li::before{content:"";position:absolute;left:0;top:5px;border-left:10px solid var(--ink);border-top:6px solid transparent;border-bottom:6px solid transparent}
  .offer-list strong{font-weight:700}
  .promo{display:inline-block;border:1.5px dashed var(--ink);border-radius:6px;padding:0 4px;line-height:16px;font-weight:700}

  .deals-rail{position:absolute;left:44px;top:838px;width:48px;height:222px;border-left:1.5px solid var(--teal);border-top:1.5px solid var(--teal);border-bottom:1.5px solid var(--teal)}
  .deals-list{position:absolute;left:26px;top:854px;width:780px;list-style:none;font-size:14px;line-height:17px}
  .deals-list li{position:relative;padding-left:46px;margin-bottom:14px}
  .deals-list li svg{position:absolute;left:0;top:1px}
  .deals-list strong{font-weight:700}

  .footer-left{position:absolute;left:0;top:1097px;width:360px;height:103px;background:linear-gradient(90deg,#1a9fae,#3fb0b3)}
  .footer-right{position:absolute;left:330px;top:1097px;width:518px;height:103px;background:var(--deep-teal);clip-path:polygon(9% 0,100% 0,100% 100%,0 100%)}
  .brand{position:absolute;left:24px;top:1126px;display:flex;align-items:center;gap:12px;color:var(--white);font-family:"Poppins",sans-serif;font-weight:600;font-size:19px;line-height:20px}
  .brand-dot{width:40px;height:40px;border-radius:50%;border:2px solid var(--white)}
  .offer-cta{position:absolute;left:350px;top:1118px;display:flex;align-items:center;gap:14px;color:var(--white);font-family:"Montserrat",sans-serif;font-weight:500;font-size:30px;letter-spacing:.5px;white-space:nowrap}
</style>
</head>
<body>
<main class="flyer">
  <div class="header-band">
    <span class="header-stripe" style="left:-30px;top:30px;width:110px;height:26px"></span>
    <span class="header-stripe" style="left:130px;top:-20px;width:140px;height:24px"></span>
    <span class="header-stripe" style="left:520px;top:10px;width:160px;height:26px"></span>
    <span class="header-stripe" style="left:620px;top:40px;width:120px;height:22px"></span>
  </div>

  <div class="photo-main" role="img" aria-label="Brass mailbox cabinet with rows of locking doors"></div>

  <div class="headline-pill"></div>
  <h1 class="headline">NOW RENTING</h1>
  <p class="subhead">MAILBOXES ON</p>
  <p class="location">MAPLE RIDGE CROSSING SHOPPING CENTER.</p>

  <p class="intro"><strong>Renting a mail box</strong> is one of the most efficient and cost saving methods for receiving your mail and packages. Instead of having to worry about private security, weather conditions, sorting, and deliveries; all you have to do is pick-up your mail from our secured facility each day except Sundays. You will get a notification when mail arrives whether envelope or package, it will be scanned in daily which other mailbox stores do not offer! We offer onsite Notary Public with no appointments and onsite Passport Photos and can ship out same day.</p>

  <div class="section-band offering-band">WE ARE OFFERING-</div>

  <div class="photo-open" role="img" aria-label="Open brass mailbox door showing the compartment inside"></div>
  <svg class="open-view" viewBox="0 0 190 60">
    <path id="arc" d="M5 12 Q95 52 185 18" fill="none"/>
    <text font-family="Montserrat, sans-serif" font-weight="800" font-size="22" fill="var(--teal-light)" letter-spacing="1"><textPath href="#arc">OPEN VIEW</textPath></text>
  </svg>

  <span class="bubble" style="left:560px;top:715px;width:20px;height:20px"></span>
  <span class="bubble" style="left:612px;top:735px;width:34px;height:34px;opacity:.7"></span>
  <span class="bubble" style="left:597px;top:783px;width:14px;height:14px"></span>

  <ul class="offer-list">
    <li>All Maple Ridge crossing shopping center owners/employees an exclusive promo deal! <span class="promo">$12 a month&nbsp; for 6-12 months leases!</span></li>
    <li>You get a mailbox in the shop,</li>
    <li>A book of <strong>stamps(20 count)</strong>,&nbsp;&nbsp; 3 notarizations by appointment, <strong>100 copies</strong> of black and white, and <strong>100 copies</strong> of color.<br>Please see associate for sign up!</li>
  </ul>

  <div class="section-band deals-band">CHECK OUT THESE OTHER DEALS!</div>
  <svg class="deals-chevron" viewBox="0 0 52 52" aria-hidden="true">
    <path d="M0 0 H14 L40 26 L14 52 H0 L26 26 Z" fill="var(--teal)"/>
    <path d="M22 0 H28 L54 26 L28 52 H22 L48 26 Z" fill="var(--teal)"/>
  </svg>

  <div class="deals-rail"></div>
  <ul class="deals-list">
    <li><svg width="12" height="9" viewBox="0 0 12 9"><rect width="12" height="9" rx="1" fill="var(--teal)"/><path d="M0.5 1 L6 5 L11.5 1" stroke="#fff" fill="none"/></svg>As a retail owner, you know how important it is to keep your customers coming back - you will get <strong>20% discount</strong> for printing services.</li>
    <li><svg width="12" height="9" viewBox="0 0 12 9"><rect width="12" height="9" rx="1" fill="var(--teal)"/><path d="M0.5 1 L6 5 L11.5 1" stroke="#fff" fill="none"/></svg>We duplicate keys for <strong>$2/each,</strong> our regular price charge is <strong>$4/each</strong>. Save up to <strong>50%!</strong></li>
    <li><svg width="12" height="9" viewBox="0 0 12 9"><rect width="12" height="9" rx="1" fill="var(--teal)"/><path d="M0.5 1 L6 5 L11.5 1" stroke="#fff" fill="none"/></svg>Lamination is also <strong>discounted at 10%</strong> off.</li>
    <li><svg width="12" height="9" viewBox="0 0 12 9"><rect width="12" height="9" rx="1" fill="var(--teal)"/><path d="M0.5 1 L6 5 L11.5 1" stroke="#fff" fill="none"/></svg><strong>10%</strong> off retail supplies ... must be minimum of 10$</li>
    <li><svg width="12" height="9" viewBox="0 0 12 9"><rect width="12" height="9" rx="1" fill="var(--teal)"/><path d="M0.5 1 L6 5 L11.5 1" stroke="#fff" fill="none"/></svg>For house accounts - a <strong>5%</strong> discount will be deducted monthly of billing change to invoicing PLUS we're giving another <strong>5%</strong> of the discount if you upgrade and sign up for mailbox. Great right?</li>
  </ul>

  <div class="footer-left"></div>
  <div class="footer-right"></div>
  <div class="brand"><span class="brand-dot"></span><span>SWIFT PARCEL<br>&amp; POST</span></div>
  <div class="offer-cta">
    <svg width="42" height="42" viewBox="0 0 42 42" aria-hidden="true" fill="none" stroke="#fff" stroke-width="3" stroke-linecap="round">
      <circle cx="21" cy="23" r="14"/>
      <path d="M21 15 V23 H27"/>
      <path d="M5 10 A7 7 0 0 1 13 4"/>
      <path d="M37 10 A7 7 0 0 0 29 4"/>
      <path d="M11 37 L8 40 M31 37 L34 40"/>
    </svg>
    <span>LIMITED TIME OFFER NOW!</span>
  </div>
</main>
</body>
</html>
```